Web site for Life Coaching Consultant

I require a website for a life coaching business. I have a Tidal Netware account which I set up last week. I will need to be able to add articles and testimonials. The design should communicate that RL Harbor Lanterns is there to help people breakdown personal barriers and that we are an advocate to help them achieve personal goals.
Updates

Reason: I have some designers just accepting my invitation to submit so to give them a few days to submit. I have been thrilled with the quality of the submissions Thank you.

Hi everyone

I am loving all your designs.  The only feedback I can get from people is that they feel that the runner makes the web page look like a personal coach rather than a life coach that helps people with relations, career, and personal road blocks.

Sorry                                   

Reason: Hi I have increased the deadline as there has been so many amazing designs and some of you have asked to fine tune your entries. I would like to take this opportunity to thank you all. It is going to be a tough decision. I have put a few more pictures on the project page hoping this will help

Hi I just wanted to thank you all for your great designs.  As I got so many good designs I have asked people to vote.  I will be in touch in the next day or 2.

Cheers

Target Market(s)

People with self esteem issues either woman or girls, people who want to goal set and need an advocate

Industry/Entity Type

Life Coaching

Colors
d2a4cc
e567a6

Requirements
Must have
• must have bio section, logo, articles page, affirmation section and testimonial page.

```html
<!DOCTYPE html>
<html lang="en">
<head>
<meta charset="utf-8">
<title>RL Harbor Lanterns — Life Coaching</title>
<link href="https://fonts.googleapis.com/css2?family=Open+Sans:ital,wght@0,400;0,600;0,700;1,400&display=swap" rel="stylesheet">
<style>
  :root {
    --pink: #e91e78;
    --pink-deep: #cc1a66;
    --pink-soft: #e567a6;
    --lilac: #d2a4cc;
    --rule: #c4c4c4;
    --nav-grey: #7a7a7a;
    --body-grey: #555555;
    --white: #ffffff;
  }
  * { box-sizing: border-box; margin: 0; padding: 0; }
  html, body {
    width: 1200px; height: 1091px; overflow: hidden;
    background: var(--white);
    font-family: "Open Sans", Arial, sans-serif;
  }
  .page { position: relative; width: 1200px; height: 1091px; }

  .header-rule {
    position: absolute; top: 121px; height: 1px; background: var(--rule);
  }
  .header-rule.left { left: 0; width: 90px; }
  .header-rule.right { left: 315px; right: 0; }

  .brand {
    position: absolute; left: 90px; top: 40px; width: 225px;
    display: flex; flex-direction: column; align-items: center; gap: 8px;
  }
  .brand-dot {
    width: 44px; height: 44px; border-radius: 50%; background: var(--pink);
  }
  .brand-name {
    color: var(--pink); font-weight: 600; font-size: 21px; white-space: nowrap;
  }

  .main-nav {
    position: absolute; top: 47px; left: 560px;
    display: flex; gap: 0;
  }
  .main-nav a {
    display: block; height: 37px; line-height: 37px; padding: 0 11px;
    margin-right: 13px;
    color: var(--nav-grey); font-weight: 700; font-size: 15px;
    text-decoration: none; border-radius: 4px;
  }
  .main-nav a.active { background: var(--pink); color: var(--white); }

  .affirmation {
    position: absolute; left: 125px; top: 182px; width: 950px; height: 96px;
    border-radius: 10px;
    background: linear-gradient(90deg, var(--pink-deep), var(--pink-soft) 55%, var(--pink-deep) 75%, var(--pink-soft));
    opacity: .85;
  }

  .section-rule {
    position: absolute; top: 338px; left: 0; width: 1200px; height: 1px; background: var(--rule);
  }

  .bio {
    position: absolute; left: 142px; top: 364px; width: 430px;
  }
  .bio h2 {
    color: var(--pink); font-size: 20px; font-weight: 700; text-transform: uppercase;
    margin-bottom: 8px;
  }
  .bio p {
    color: var(--body-grey); font-size: 14px; line-height: 26px;
    margin-bottom: 26px;
  }

  .bio-photo {
    position: absolute; left: 634px; top: 375px; width: 421px; height: 281px;
    border: 1px solid var(--rule); padding: 2px; background: var(--white);
  }
  .bio-photo .fill {
    width: 100%; height: 100%;
    background: linear-gradient(180deg, #1d5fa8 0%, #3f8fd0 40%, #34c3cf 52%, #d9e6e4 70%, #eceae3 100%);
  }

  .testimonials {
    position: absolute; left: 0; top: 693px; width: 1200px; height: 235px;
    background: linear-gradient(90deg, #ea3a86 0%, #d41f6c 50%, #cf1d67 75%, #e0307f 100%);
    text-align: center; color: var(--white);
  }
  .testimonials blockquote {
    margin: 45px auto 0; width: 800px;
    font-style: italic; font-size: 26px; line-height: 35px; letter-spacing: -0.3px;
  }
  .testimonials cite {
    display: block; margin-top: 20px; font-style: normal; font-weight: 700; font-size: 18px;
  }
  .slider-dots {
    position: absolute; left: 0; right: 0; top: 903px; top: 210px;
    display: flex; justify-content: center; gap: 2px;
  }
  .slider-dots span {
    width: 10px; height: 10px; border-radius: 50%; border: 1.5px solid var(--white);
  }
  .slider-dots span.on { background: var(--white); }
</style>
</head>
<body>
<div class="page">
  <header>
    <div class="header-rule left"></div>
    <div class="header-rule right"></div>
    <div class="brand">
      <span class="brand-dot"></span>
      <span class="brand-name">RL Harbor Lanterns</span>
    </div>
    <nav class="main-nav">
      <a class="active" href="#">HOME</a>
      <a href="#">ABOUT US</a>
      <a href="#">ARTICLES</a>
      <a href="#">TESTIMONIALS</a>
      <a href="#">CONTACT</a>
    </nav>
  </header>

  <div class="affirmation" role="img" aria-label="Hand-lettered affirmation: Dream Big, Set Goals, Take Action"></div>

  <div class="section-rule"></div>

  <section class="bio">
    <h2>This is a content header</h2>
    <p>Lorem ipsum dolor sit amet, at eum altera graecis tacimates. Simul eleifend an mea, vel ex affert alterum. Ad quo fugit invenire interesset. Qui at quot partem maluisset, augue dicant everti nam te, quando persequeris ei usu.</p>
    <p>Rebum appetere forensibus vis no, eam cu veri euripidis gloriatur, pri erat eripuit dissentiunt ea. Ea postea sanctus adversarium per. Tale dicta ius ne, sit at choro nusquam appellantur. Et legere commodo mediocrem vis, te probo mollis delicata vel. Ut delenit lucilius phaedrum mel. Nobis percipitur nam an.</p>
  </section>

  <figure class="bio-photo">
    <div class="fill" role="img" aria-label="Photo of a tropical beach with turquoise water and a jetty under a blue sky"></div>
  </figure>

  <section class="testimonials" role="region" aria-label="Testimonials">
    <blockquote>"Lorem ipsum dolor sit amet, at eum altera graecis tacimates. Simul eleifend an mea, vel ex affert alterum. Ad quo fugit invenire interesset."</blockquote>
    <cite>- Maya Linden</cite>
    <div class="slider-dots">
      <span class="on"></span><span></span><span></span><span></span>
    </div>
  </section>
</div>
</body>
</html>
```